Sonne im Glas
Zielgruppe
Wir sind ein kleines Weingut in einer kleinen Ortschaft am Neusiedlersee | Burgenland | Österreich und produzieren auf unseren Weingartenflächen zertifizierte Bioweine.
Die Zielgruppe für diesen außergewöhnlichen Wein sind Weininteressierte im mittleren Alter.
Aufgabenstellung
Name des Weines: 'Sonne im Glas'
Es handelt sich um einen Wein einer lokalen Sorte der nach der händischen Ernte und Spontanvergärung von September bis Juni des folgenden Jahres (also 10 Monate) auf der Feinhefe und ohne Eingriffe gelagert hat. Dannach erfolgt die Füllung ohne Filtration.
Dementsprechend chillig, vielschichtig und harmonisch präsentiert sich dieser Wein jetzt nach der Füllung in Burgunderflaschen.
Etikettendimension soll in der Richtung: 100 x 80 (HxB) liegen, wobei die Höhe mit 100 mm begrenzend ist.

```html
<!DOCTYPE html>
<html lang="de">
<head>
<meta charset="utf-8">
<title>Sonne im Glas – Etikettenentwürfe</title>
<link rel="stylesheet" href="https://fonts.googleapis.com/css2?family=Sacramento&family=Raleway:wght@200&family=Open+Sans:wght@300&display=swap">
<style>
  :root {
    --wine-red: #a0002a;
    --label-white: #ffffff;
    --frame-line: rgba(255, 255, 255, 0.55);
    --page-bg: #ffffff;
  }
  * { margin: 0; padding: 0; box-sizing: border-box; }
  html, body {
    width: 1200px;
    height: 1200px;
    overflow: hidden;
    background: var(--page-bg);
  }
  .canvas {
    position: relative;
    width: 1200px;
    height: 1200px;
    display: flex;
    flex-direction: column;
    align-items: center;
    justify-content: center;
    gap: 40px;
  }
  .label {
    position: relative;
    width: 680px;
    height: 544px;
    background: var(--wine-red);
    color: var(--label-white);
    overflow: hidden;
  }

  /* Variante 1: Schreibschrift über Versalien */
  .label--headline .script-line {
    position: absolute;
    left: 20px;
    right: 20px;
    top: 60px;
    text-align: center;
    font-family: 'Sacramento', cursive;
    font-weight: 400;
    font-size: 190px;
    line-height: 1;
    white-space: nowrap;
    z-index: 2;
  }
  .label--headline .caps-line {
    position: absolute;
    left: 0;
    right: 0;
    top: 250px;
    text-align center;
    text-align: center;
    font-family: 'Raleway', sans-serif;
    font-weight: 200;
    font-size: 190px;
    line-height: 1;
    letter-spacing: 4px;
    z-index: 1;
  }
  .tagline {
    position: absolute;
    left: 0;
    right: 0;
    text-align: center;
    font-family: 'Open Sans', sans-serif;
    font-weight: 300;
    text-transform: uppercase;
    white-space: nowrap;
  }
  .label--headline .tagline {
    top: 482px;
    font-size: 16px;
    letter-spacing: 0.3px;
  }

  /* Variante 2: gestapelte Schreibschrift im Rahmen */
  .label--stacked .inner-frame {
    position: absolute;
    inset: 22px 20px;
    border: 1px solid var(--frame-line);
  }
  .label--stacked .stacked-words {
    position: absolute;
    left: 0;
    right: 0;
    top: 50px;
    text-align: center;
    font-family: 'Sacramento', cursive;
    font-weight: 400;
    font-size: 120px;
    line-height: 124px;
  }
  .label--stacked .stacked-words span { display: block; }
  .label--stacked .tagline {
    top: 494px;
    font-size: 8px;
    letter-spacing: 0.2px;
  }
</style>
</head>
<body>
  <main class="canvas">
    <section class="label label--headline" aria-label="Etikett Variante 1">
      <div class="script-line">Sonne im</div>
      <div class="caps-line">GLAS</div>
      <p class="tagline">Sonnig. Ungefiltert. Naturbelassen.</p>
    </section>

    <section class="label label--stacked" aria-label="Etikett Variante 2">
      <div class="inner-frame"></div>
      <h1 class="stacked-words">
        <span>sonne</span>
        <span>im</span>
        <span>glas</span>
      </h1>
      <p class="tagline">Sonnig. Ungefiltert. Naturbelassen.</p>
    </section>
  </main>
</body>
</html>
```